Termite Mailer September 2021

We need a clean modern looking flyer advertising termites via the mail.

Size should be 9"x6"

Our tagline is "The Smarter Approach to Pest Control"

Something along the stylistic design of these:

https://pics.hollowmarsh.example/Qa83LkTzWp

https://pics.hollowmarsh.example/Rn47VbXcMd

https://pics.hollowmarsh.example/Hj29PsYeUf

https://www.flintquillprint.example/wp-content/uploads/designs/img/Pest-Prevention-Postcard-PST-1003.jpg

Should include some of this verbiage:

HAVE YOU SCHEDULED YOUR ANNUAL TERMITE INSPECTION? - MAKE IT IN RED

DON'T WAIT. PROTECT YOUR HOME TODAY!

ABSOLUTELY FREE INSPECTION. NO OBLIGATION.

TERMITES CAN CAUSE SEVERE DAMAGE TO YOUR HOME.

BRINDLEVALE LOGO

THE SMARTER APPROACH TO PEST CONTROL.

PROTECT YOUR MOST VALUABLE ASSET.

10% DISCOUNT ON ANY SERVICE GUARANTEED IF YOU CALL TODAY.

INCLUDE A PICTURE OF A TERMITE AS WELL SOMEWHERE AND WOOD DAMAGE.

Target Market(s)

Homeowners in Southern California USA

Industry/Entity Type

Pest Control/Extermination

Font styles to use
Other font styles liked:
• Chaparral Pro Italic, Brava Slab

Requirements
Must have
• Clean design, picture of house, picture of Termite, 10% off coupon and call to action on the back
Should not have
• Bad looking houses, colors that don't match our logo

```html
<!DOCTYPE html>
<html lang="en">
<head>
<meta charset="utf-8">
<title>Brindlevale Termite Mailer</title>
<link href="https://fonts.googleapis.com/css2?family=Bree+Serif&family=Oswald:wght@300;400;500&display=swap" rel="stylesheet">
<style>
  :root{
    --sky:#4a84c1;
    --teal:#4f9aa4;
    --sea:#58aa89;
    --band-green:#7ac143;
    --badge-blue:#1b6db5;
    --brand-blue:#1b6db5;
    --brand-green:#7ac143;
    --headline:#ffffff;
    --question:#ffe600;
    --paper:#ffffff;
  }
  *{margin:0;padding:0;box-sizing:border-box}
  html,body{width:1200px;height:800px;overflow:hidden;background:var(--paper)}
  .mailer{position:relative;width:1200px;height:800px;overflow:hidden;
    background:linear-gradient(180deg,var(--sky) 0%,var(--teal) 45%,var(--sea) 80%);}
  .headline{position:absolute;left:74px;top:104px;color:var(--headline);
    font-family:"Bree Serif",Georgia,serif;font-weight:400;font-size:56px;line-height:52px;letter-spacing:2px;}
  .question{position:absolute;left:284px;top:262px;color:var(--question);
    font-family:"Bree Serif",Georgia,serif;font-size:24px;line-height:26px;letter-spacing:2.4px;}
  .question .accent{color:var(--headline)}
  .perks{position:absolute;left:62px;top:437px;list-style:none;color:var(--headline);
    font-family:"Bree Serif",Georgia,serif;font-size:26px;line-height:28px;letter-spacing:2.2px;}
  .perks li{margin-bottom:6px;padding-left:14px;position:relative}
  .perks li::before{content:"";position:absolute;left:0;top:9px;width:5px;height:5px;border-radius:50%;background:var(--headline)}
  .collage{position:absolute;left:0;top:0}
  .callout{position:absolute;width:138px;height:138px;border:2px solid var(--paper);border-radius:50%;
    color:var(--paper);font-family:"Oswald","Arial Narrow",sans-serif;font-weight:300;font-size:16px;line-height:18.5px;
    display:flex;align-items:center;padding-left:22px;letter-spacing:0.9px}
  .callout--damage{left:499px;top:113px}
  .callout--asset{left:883px;top:39px}
  .cta-band{position:absolute;left:0;top:626px;width:1200px;height:98px;background:var(--band-green)}
  .contact{position:absolute;left:74px;top:626px;color:var(--paper);font-family:"Oswald","Arial Narrow",sans-serif;
    font-weight:500;display:flex;align-items:baseline;gap:24px}
  .contact__label{font-size:44px}
  .contact__phone{font-size:70px;letter-spacing:1px}
  .badge{position:absolute;left:737px;top:586px}
  .badge-value{position:absolute;left:737px;top:640px;width:121px;text-align:center;color:var(--paper);
    font-family:"Oswald","Arial Narrow",sans-serif;font-weight:500;font-size:56px;line-height:66px}
  .discount{position:absolute;left:873px;top:644px;color:var(--paper);font-family:"Oswald","Arial Narrow",sans-serif;
    font-weight:400;font-size:25px;line-height:26px;letter-spacing:0}
  .footer{position:absolute;left:0;top:724px;width:1200px;height:76px;background:var(--paper);
    display:flex;align-items:center}
  .brand{position:absolute;left:70px;display:flex;align-items:center;gap:10px;
    font-family:"Bree Serif",Georgia,serif;font-size:26px;color:var(--brand-blue);letter-spacing:0.5px}
  .brand__mark{width:38px;height:38px;border-radius:50%;background:var(--brand-green)}
  .tagline{position:absolute;left:313px;font-family:"Bree Serif",Georgia,serif;font-size:29px;color:var(--brand-blue);letter-spacing:1.1px}
  .website{position:absolute;left:897px;font-family:"Bree Serif",Georgia,serif;font-size:19px;color:var(--brand-blue);letter-spacing:3.2px}
</style>
</head>
<body>
<div class="mailer">

  <svg class="collage" width="1200" height="800" viewBox="0 0 1200 800">
    <defs>
      <linearGradient id="woodDamage" x1="0" y1="0" x2="1" y2="1">
        <stop offset="0" stop-color="#8a6a52"/><stop offset="0.5" stop-color="#b39a80"/><stop offset="1" stop-color="#5a3f2c"/>
      </linearGradient>
      <linearGradient id="housePhoto" x1="0" y1="0" x2="0" y2="1">
        <stop offset="0" stop-color="#3f7fc8"/><stop offset="0.45" stop-color="#8d8f8a"/><stop offset="0.8" stop-color="#c9b79a"/><stop offset="1" stop-color="#9aa59a"/>
      </linearGradient>
      <linearGradient id="termiteSoil" x1="0" y1="0" x2="1" y2="1">
        <stop offset="0" stop-color="#6a4a34"/><stop offset="0.5" stop-color="#caa77e"/><stop offset="1" stop-color="#3d281c"/>
      </linearGradient>
      <linearGradient id="tunnelledWood" x1="0" y1="0" x2="1" y2="1">
        <stop offset="0" stop-color="#d9d4cc"/><stop offset="0.5" stop-color="#7a5a44"/><stop offset="1" stop-color="#4a3426"/>
      </linearGradient>
      <linearGradient id="colonySoil" x1="0" y1="0" x2="1" y2="1">
        <stop offset="0" stop-color="#5a3a28"/><stop offset="0.5" stop-color="#a9825c"/><stop offset="1" stop-color="#6b4a33"/>
      </linearGradient>
    </defs>

    <g stroke="#ffffff" stroke-width="3" stroke-linejoin="miter">
      <polygon role="img" aria-label="Photo of termite-damaged timber" points="573,626 573,320 764,193 955,320 955,626" fill="url(#woodDamage)"/>
      <polygon role="img" aria-label="Photo of a modern two-storey family home" points="764,626 764,320 955,193 1145,320 1145,626" fill="url(#housePhoto)"/>
      <polygon role="img" aria-label="Close-up photo of a termite on soil" points="477,626 477,475 573,410 666,475 666,626" fill="url(#termiteSoil)"/>
      <polygon role="img" aria-label="Photo of a gloved hand holding tunnelled wood" points="666,626 666,475 764,410 857,475 857,626" fill="url(#tunnelledWood)"/>
      <polygon role="img" aria-label="Photo of a termite colony in the ground" points="857,626 857,475 955,410 1048,475 1048,626" fill="url(#colonySoil)"/>
      <line x1="573" y1="475" x2="573" y2="626"/>
      <line x1="955" y1="475" x2="955" y2="626"/>
    </g>

    <g class="outline-house">
      <polyline points="439,626 376,626 376,568 414,543 475,543" fill="none" stroke="#ffffff" stroke-width="3"/>
      <line x1="376" y1="568" x2="439" y2="568" stroke="#ffffff" stroke-width="3"/>
      <polygon points="439,626 439,568 475,543 512,568 512,626" fill="#ffffff"/>
      <path d="M462,626 V590 a13,13 0 0 1 26,0 V626 Z" fill="var(--sea)"/>
    </g>

    <g class="connectors" fill="none" stroke="#ffffff" stroke-width="1.5">
      <polyline points="638,182 682,182 682,346"/>
      <polyline points="1020,108 1064,108 1064,346"/>
      <polyline points="417,353 542,353 542,480"/>
    </g>
    <g fill="#ffffff">
      <circle cx="682" cy="346" r="6"/>
      <circle cx="1064" cy="346" r="6"/>
      <circle cx="542" cy="480" r="6"/>
    </g>
  </svg>

  <h1 class="headline">DON'T WAIT.<br>PROTECT<br>YOUR HOME<br>TODAY!</h1>

  <p class="question">HAVE YOU<br>SCHEDULED<br>YOUR ANNUAL<br><span class="accent">TERMITE</span><br>INSPECTION?</p>

  <ul class="perks">
    <li>ABSOLUTELY<br>FREE INSPECTION</li>
    <li>NO OBLIGATION</li>
  </ul>

  <p class="callout callout--damage">TERMITES CAN<br>CAUSE SEVERE<br>DAMAGE TO<br>YOUR HOME.</p>
  <p class="callout callout--asset">PROTECT<br>YOUR MOST<br>VALUABLE<br>ASSET.</p>

  <div class="cta-band"></div>
  <p class="contact"><span class="contact__label">CONTACT US:</span><span class="contact__phone">555 014 2738</span></p>

  <svg class="badge" width="121" height="138" viewBox="0 0 121 138">
    <polygon points="0,138 0,40 60.5,0 121,40 121,138" fill="var(--badge-blue)"/>
  </svg>
  <p class="badge-value">10%</p>
  <p class="discount">DISCOUNT ON ANY SERVICE<br>GUARANTEED<br>IF YOU CALL TODAY.</p>

  <footer class="footer">
    <div class="brand"><span class="brand__mark"></span><span class="brand__name">BRINDLEVALE</span></div>
    <p class="tagline">The Smarter Approach to Pest Control</p>
    <p class="website">www.gobrindlevale.com</p>
  </footer>

</div>
</body>
</html>
```